Postcard Design - Thanksgiving Card - Ridgeline Thermal Coils

Here are just a few of the heating and cooling products we offer:

• Steam Coils • Convector Coils
• Hot Water Coils • Re-Heat Coils
• Chilled Water Coils • Tube Bundles
• Direct Expansion (Evaporator) Coils • Shell & Tube Heat Exchangers
• Condensing Coils • Custom Coils to end user spec.’s

ENGINEERING - We can duplicate any existing equipment, even equipment that has been obsolete for years. Ridgeline Thermal personnel will come directly to your job site and match-up dimensions, materials, and performance - all free of charge. We can build from copper, aluminum, cupro-nickel, brass, and more. Heat exchangers and tube bundles can be replaced & warranted as new with great savings; this includes Hart & Pemberly, Wendover-Voss, Lumo, and others. We also make engineering recommendations and suggestions regarding the correct ways to replace equipment or methods of increasing the life expectancy of equipment. We will help solve your HVAC problems, not duplicate them.

```html
<!DOCTYPE html>
<html lang="en">
<head>
<meta charset="utf-8">
<title>Ridgeline Thermal Coils – Thanksgiving Postcard</title>
<link href="https://fonts.googleapis.com/css2?family=Nunito+Sans:wght@400;700;800&family=Tinos:wght@400;700&family=Great+Vibes&family=Allura&display=swap" rel="stylesheet">
<style>
  :root{
    --backdrop:#ececec;
    --card:#ffffff;
    --brand-blue:#0a74bf;
    --brand-purple:#2e3192;
    --photo-dark:#4f6f86;
    --photo-light:#b9c6cf;
    --ink:#1b1b1b;
    --autumn:#f0962a;
    --white:#ffffff;
  }
  *{margin:0;padding:0;box-sizing:border-box}
  html,body{width:1200px;height:1000px;overflow:hidden;background:var(--backdrop)}
  body{position:relative;font-family:"Nunito Sans",Arial,sans-serif;color:var(--ink)}

  .postcard{position:absolute;background:var(--card);box-shadow:8px 8px 8px rgba(0,0,0,.45)}
  .postcard--front{left:155px;top:62px;width:517px;height:400px;overflow:hidden}
  .postcard--back{left:467px;top:488px;width:571px;height:442px}

  .front-art{position:absolute;left:0;top:0}
  .front-pitch{position:absolute;right:27px;top:22px;width:300px;text-align:right;color:var(--white);font-size:11px;line-height:15.5px}
  .front-pitch strong{display:block;font-size:14.5px;font-weight:800;letter-spacing:.5px;margin-top:5px}

  .badge{position:absolute;left:21px;top:0;width:171px;height:156px;filter:drop-shadow(0 2px 3px rgba(0,0,0,.35))}
  .badge svg{position:absolute;inset:0}
  .badge-content{position:absolute;left:0;top:26px;width:171px;text-align:center;font-family:"Tinos","Times New Roman",serif}

  .brand{display:flex;align-items:center;justify-content:center;gap:5px;font-family:"Tinos","Times New Roman",serif;font-weight:700;color:var(--ink);text-transform:uppercase;letter-spacing:.3px}
  .brand-square{width:9px;height:9px;background:var(--ink)}
  .brand--front{font-size:11.5px}
  .tagline{font-family:"Tinos","Times New Roman",serif;font-size:7.5px;letter-spacing:.2px;margin-top:6px}
  .partners{font-family:"Tinos","Times New Roman",serif;font-size:11px;letter-spacing:.4px;margin-top:12px}
  .address{font-family:"Tinos","Times New Roman",serif;font-size:9.5px;margin-top:5px}

  .offer{position:absolute;left:0;top:268px;width:517px;text-align:center;color:var(--white)}
  .offer h2{font-size:14.5px;font-weight:800;letter-spacing:.6px;margin-bottom:2px}
  .offer ul{list-style:none;font-size:11.5px;line-height:17px}

  .contact-bar{position:absolute;left:0;bottom:0;width:517px;height:35px;display:flex;align-items:center;justify-content:center;font-size:13px;letter-spacing:.4px}
  .contact-bar strong{font-weight:800;margin-right:4px}

  .back-header{position:absolute;left:63px;top:8px;width:150px;text-align:center}
  .brand--back{font-size:11px;margin-top:28px}
  .back-header .tagline{margin-top:10px;margin-bottom:18px}
  .back-details{position:absolute;left:13px;top:104px;width:260px;text-align:center;font-size:9.5px;line-height:15px}
  .back-details .partners{margin-top:0;font-size:11px;line-height:16px}

  .greeting{position:absolute;left:18px;top:170px;width:250px;text-align:center;font-family:"Great Vibes",cursive;font-size:36px;color:var(--autumn);letter-spacing:-1px}
  .message{position:absolute;left:18px;top:235px;width:250px;text-align:center;font-size:11px;line-height:16px}
  .signature{position:absolute;left:18px;top:332px;width:250px;text-align:center;font-family:"Allura",cursive;font-size:20px}
</style>
</head>
<body>

<section class="postcard postcard--front" aria-label="Postcard front">
  <svg class="front-art" width="517" height="400" viewBox="0 0 517 400">
    <defs>
      <linearGradient id="photoTone" x1="0" y1="0" x2="1" y2="0">
        <stop offset="0" stop-color="var(--photo-dark)"/>
        <stop offset=".5" stop-color="var(--photo-light)"/>
        <stop offset="1" stop-color="#8a9aa6"/>
      </linearGradient>
    </defs>
    <rect width="517" height="365" fill="var(--brand-blue)"/>
    <path d="M0 113 C150 90 320 110 517 150 L517 300 L0 300 Z" fill="var(--brand-purple)"/>
    <path d="M0 228 C160 175 330 140 517 138 L517 300 L0 300 Z" fill="url(#photoTone)" role="img" aria-label="Photo of industrial HVAC coil equipment and a plant floor"/>
    <path d="M0 283 C120 252 330 248 517 270 L517 365 L0 365 Z" fill="var(--brand-blue)"/>
  </svg>

  <div class="badge">
    <svg width="171" height="156" viewBox="0 0 171 156"><polygon points="0,0 171,0 171,138 86,156 0,138" fill="var(--white)"/></svg>
    <div class="badge-content">
      <div class="brand brand--front"><span class="brand-square"></span>Ridgeline Thermal Coils</div>
      <div class="tagline">HVACR COILS • HEAT EXCHANGERS</div>
      <div class="partners">DALE MERCER &amp; RUSS OKAFOR</div>
      <div class="address">Brookvale, MI 48990. P.O. Box 718</div>
    </div>
  </div>

  <p class="front-pitch">Duplicate any existing equipment,<br>even equipment that has been obsolete for years.<br>Ridgeline Thermal personnel will come directly<br>to your job site and match-up dimensions,<br>materials, and performance<strong>ALL FREE OF CHARGE</strong></p>

  <div class="offer">
    <h2>WE OFFER:</h2>
    <ul>
      <li>• Steam Coils • Convector Coils • Hot Water Coils</li>
      <li>• Re-Heat Coils • Chilled Water Coils • Tube Bundles</li>
      <li>• Direct Expansion (Evaporator) Coils • Shell &amp; Tube Heat Exchangers</li>
      <li>• Condensing Coils • Custom Coils to end user spec.’s</li>
    </ul>
  </div>

  <div class="contact-bar"><strong>CONTACT US: 888 - 555 - 0147</strong>| Email: coilpro@ridgelinemail.net</div>
</section>

<section class="postcard postcard--back" aria-label="Postcard back">
  <div class="back-header">
    <div class="brand brand--back"><span class="brand-square"></span>Ridgeline Thermal Coils</div>
    <div class="tagline">HVACR COILS • HEAT EXCHANGERS</div>
  </div>
  <div class="back-details">
    <div class="partners">DALE MERCER &amp; RUSS OKAFOR</div>
    <div>Brookvale, MI 48990. P.O. Box 718</div>
    <div>Phone: 888 - 555 - 0147</div>
    <div>Email: coilpro@ridgelinemail.net</div>
  </div>
  <h1 class="greeting">Happy Thanksgiving</h1>
  <p class="message">It is the time of year for remembering everything that makes us grateful. That is why we want to express our appreciation for your confidence in our firm to assist you on your jobsite or at your facility to solve a coil or heat exchanger problem.</p>
  <p class="signature">Dale &amp; Russ</p>
</section>

</body>
</html>
```